Business cards for Home & Garden Design business
Oakvale Grove Design
Business cards for Home & Garden Design business - Home and Garden
Creative Brief
Bright & Fun-filled
Marla Pendby
Designer
PO Box 732 Winkler, MB R6W 2K9
marlapendby@oakvalegrovedesign.example
oakvalegrovedesign.example
Would love to have my logo on a background of a rustic, white fence/door, or white birch trees. Question - do you already have access to my logo, or how do I upload it?

```html
<!DOCTYPE html>
<html lang="en">
<head>
<meta charset="utf-8">
<title>Oakvale Grove Design – Business Cards</title>
<link href="https://fonts.googleapis.com/css2?family=Open+Sans:wght@400;600;700&display=swap" rel="stylesheet">
<style>
  :root {
    --backdrop: #c9c9c9;
    --card-white: #f7f7f7;
    --card-dark: #2b2b2e;
    --teal: #4fb3b5;
    --teal-light: #8fd3d4;
    --ink: #2a2a2a;
    --ink-soft: #4a4a4a;
    --white: #ffffff;
  }
  * { margin: 0; padding: 0; box-sizing: border-box; }
  html, body { width: 1200px; height: 895px; overflow: hidden; }
  body {
    background: var(--backdrop);
    font-family: "Open Sans", Arial, sans-serif;
    position: relative;
  }
  .card {
    position: absolute;
    width: 600px;
    height: 343px;
    border-radius: 4px;
    box-shadow: 0 6px 18px rgba(0,0,0,0.18);
    overflow: hidden;
  }

  /* Back of card */
  .card-back {
    left: 540px; top: 80px;
    background: var(--card-dark);
  }
  .web-tab {
    position: absolute;
    left: 0; top: 156px;
    width: 250px; height: 30px;
    background: var(--teal);
    border-radius: 0 15px 15px 0;
    color: var(--white);
    font-size: 13px;
    font-weight: 600;
    display: flex; align-items: center;
    padding-left: 16px;
  }
  .brand-back {
    position: absolute;
    left: 290px; top: 118px;
    display: flex; align-items: center; gap: 12px;
    color: var(--teal-light);
  }

  /* Shared brand lockup */
  .brand-mark {
    width: 28px; height: 28px;
    border-radius: 50%;
    background: currentColor;
    flex: none;
  }
  .brand-name {
    font-size: 30px;
    font-weight: 600;
    line-height: 1.05;
  }

  /* Front of card */
  .card-front {
    left: 60px; top: 470px;
    background: var(--card-white);
  }
  .brand-front {
    position: absolute;
    left: 34px; top: 34px;
    display: flex; align-items: center; gap: 12px;
    color: var(--teal);
  }
  .holder {
    position: absolute;
    left: 34px; top: 160px;
    font-size: 19px;
    font-weight: 700;
    color: var(--ink);
    white-space: nowrap;
  }
  .holder .divider { font-weight: 400; margin: 0 8px; }
  .holder .role { font-weight: 400; font-size: 15px; color: var(--ink-soft); }
  .contact {
    position: absolute;
    left: 34px;
    display: flex; align-items: center; gap: 8px;
    font-size: 13px;
    color: var(--ink);
    white-space: nowrap;
  }
  .contact-address { top: 206px; }
  .contact-phones { top: 236px; }
  .contact-phones .gap { width: 22px; }
  .icon {
    width: 18px; height: 18px;
    border-radius: 50%;
    background: var(--ink);
    display: inline-flex; align-items: center; justify-content: center;
    flex: none;
  }
  .icon svg { width: 10px; height: 10px; }
  .email-band {
    position: absolute;
    left: 20px; right: 20px; top: 276px;
    height: 32px;
    border-radius: 16px;
    background: var(--ink);
    color: var(--white);
    font-size: 13px;
    display: flex; align-items: center; justify-content: flex-end;
    gap: 8px;
    padding-right: 20px;
    white-space: nowrap;
  }
  .email-band .icon { background: var(--white); }
</style>
</head>
<body>

  <section class="card card-back" aria-label="Business card back">
    <div class="web-tab">oakvalegrovedesign.example</div>
    <div class="brand-back">
      <span class="brand-mark"></span>
      <span class="brand-name">Oakvale Grove<br>Design</span>
    </div>
  </section>

  <section class="card card-front" aria-label="Business card front">
    <div class="brand-front">
      <span class="brand-mark"></span>
      <span class="brand-name">Oakvale Grove<br>Design</span>
    </div>

    <p class="holder">Marla Pendby<span class="divider">|</span><span class="role">Designer</span></p>

    <p class="contact contact-address">
      <span class="icon"><svg viewBox="0 0 10 10"><path d="M5 0.5a3.2 3.2 0 0 0-3.2 3.2C1.8 6 5 9.5 5 9.5s3.2-3.5 3.2-5.8A3.2 3.2 0 0 0 5 0.5zm0 4.5a1.3 1.3 0 1 1 0-2.6 1.3 1.3 0 0 1 0 2.6z" fill="#fff"/></svg></span>
      PO Box 000, Fernbrook Example Region
    </p>

    <p class="contact contact-phones">
      <span class="icon"><svg viewBox="0 0 10 10"><path d="M2.2 0.8l1.4 1.6-.8 1.2a6 6 0 0 0 3.6 3.6l1.2-.8 1.6 1.4-.9 1.4C4.6 9 1 5.4.8 1.7z" fill="#fff"/></svg></span>
      012 555 0147
      <span class="gap"></span>
      <span class="icon"><svg viewBox="0 0 10 10"><path d="M2.2 0.8l1.4 1.6-.8 1.2a6 6 0 0 0 3.6 3.6l1.2-.8 1.6 1.4-.9 1.4C4.6 9 1 5.4.8 1.7z" fill="#fff"/></svg></span>
      012 555 0148
    </p>

    <div class="email-band">
      <span class="icon"><svg viewBox="0 0 10 10"><rect x="1" y="2.2" width="8" height="5.6" fill="none" stroke="#2a2a2a" stroke-width="1"/><path d="M1 2.4l4 3 4-3" fill="none" stroke="#2a2a2a" stroke-width="1"/></svg></span>
      marlapendby@oakvalegrovedesign.example
    </div>
  </section>

</body>
</html>
```